Wholesale in Gold Jewellery & Gold Bullion

We are an established gold jewellery and gold bullion wholesaler selling these products to international clients. We already have a name and logo of our company, hence please view attached current card design. We need a completely new design to compliment our business and industry and the final design should be new and elegant.

Contact Information for Business Card

New card details must be same as per current card. Like logo, name, tel no. & etc.

Colors

Designer to choose colors to be used in the design.

```html
<!DOCTYPE html>
<html lang="en">
<head>
<meta charset="utf-8">
<title>Aurelin &amp; Co Business Card</title>
<link href="https://fonts.googleapis.com/css2?family=Roboto:wght@400;500;700&display=swap" rel="stylesheet">
<style>
  :root {
    --gold: #e0960c;
    --ink: #111111;
    --text: #4a4a4a;
    --rule: #8a8a8a;
    --paper: #ffffff;
    --backdrop: #e2e2e2;
  }
  * { margin: 0; padding: 0; box-sizing: border-box; }
  html, body {
    width: 1125px; height: 1200px; overflow: hidden;
    background: var(--backdrop);
    font-family: "Roboto", Arial, sans-serif;
  }
  .canvas { position: relative; width: 1125px; height: 1200px; }
  .card {
    position: absolute; left: 171px; width: 826px; height: 472px;
    box-shadow: 0 2px 4px rgba(0,0,0,0.25);
    overflow: hidden;
  }
  .card--front { top: 106px; background: var(--paper); }
  .card--back { top: 639px; background: var(--gold); }

  .brand { position: absolute; left: 241px; top: 54px; display: flex; align-items: center; gap: 16px; }
  .brand__dot { width: 84px; height: 84px; border-radius: 50%; background: var(--gold); }
  .brand__name { font-weight: 700; font-size: 33px; color: var(--ink); letter-spacing: 0.2px; white-space: nowrap; }

  .person { position: absolute; left: 39px; top: 242px; }
  .person__name { font-weight: 500; font-size: 29px; color: var(--gold); line-height: 1.1; }
  .person__role { font-weight: 500; font-size: 20px; color: var(--ink); margin-top: 4px; }

  .divider { position: absolute; left: 42px; top: 314px; width: 731px; height: 1.5px; background: var(--rule); }

  .contacts { position: absolute; left: 42px; top: 330px; list-style: none; }
  .contacts li { display: flex; align-items: center; height: 26px; font-size: 20px; color: var(--text); }
  .contacts svg { width: 20px; height: 20px; margin-right: 12px; fill: var(--gold); flex: none; }

  .address { position: absolute; right: 53px; top: 382px; text-align: right; font-size: 20px; line-height: 26px; color: var(--text); }

  .edge-band { position: absolute; left: 0; bottom: 0; width: 826px; height: 12px; }

  .back-mark { position: absolute; left: 0; right: 0; top: 150px; display: flex; flex-direction: column; align-items: center; gap: 28px; }
  .back-mark__dot { width: 90px; height: 90px; border-radius: 50%; background: var(--paper); }
  .back-mark__name { font-weight: 700; font-size: 40px; color: var(--paper); letter-spacing: 1px; }
  .web { position: absolute; left: 0; right: 0; top: 388px; text-align: center; font-size: 20px; letter-spacing: 7px; color: var(--paper); }
</style>
</head>
<body>
<div class="canvas">
  <section class="card card--front">
    <div class="brand">
      <div class="brand__dot"></div>
      <div class="brand__name">AURELIN &amp; CO PTE LTD</div>
    </div>

    <div class="person">
      <div class="person__name">Ravin Solanki</div>
      <div class="person__role">Director</div>
    </div>

    <div class="divider"></div>

    <ul class="contacts">
      <li><svg viewBox="0 0 24 24"><path d="M6.6 10.8a15.1 15.1 0 0 0 6.6 6.6l2.2-2.2c.3-.3.7-.4 1-.2 1.1.4 2.3.6 3.6.6.6 0 1 .4 1 1V20c0 .6-.4 1-1 1C10.6 21 3 13.4 3 4c0-.6.4-1 1-1h3.5c.6 0 1 .4 1 1 0 1.3.2 2.5.6 3.6.1.3 0 .7-.2 1z"/></svg>+65 6100 2400</li>
      <li><svg viewBox="0 0 24 24"><path d="M7 1h10a2 2 0 0 1 2 2v18a2 2 0 0 1-2 2H7a2 2 0 0 1-2-2V3a2 2 0 0 1 2-2zm0 3v14h10V4zm5 15.5a1 1 0 1 0 0 2 1 1 0 0 0 0-2z"/></svg>+65 9100 4521</li>
      <li><svg viewBox="0 0 24 24"><path d="M7 2h8l3 3v5H7zM4 11h16a2 2 0 0 1 2 2v7H2v-7a2 2 0 0 1 2-2zm3 4v2h10v-2z"/></svg>+65 6100 2401</li>
      <li><svg viewBox="0 0 24 24"><path d="M2 5h20v14H2zm2 2v.4l8 5.2 8-5.2V7zm0 2.8V17h16V9.8l-8 5.2z"/></svg>ravin@aurelinco.com</li>
    </ul>

    <div class="address">12 Lorong Kemuning<br>Singapore 208100</div>

    <svg class="edge-band" viewBox="0 0 826 12" preserveAspectRatio="none">
      <polygon points="0,0 534,0 530,12 0,12" fill="var(--gold)"/>
      <polygon points="540,0 826,0 826,12 536,12" fill="var(--ink)"/>
    </svg>
  </section>

  <section class="card card--back">
    <div class="back-mark">
      <div class="back-mark__dot"></div>
      <div class="back-mark__name">AURELIN &amp; CO</div>
    </div>
    <div class="web">WWW.AURELINCO.COM</div>
  </section>
</div>
</body>
</html>
```